KPT Building And Maintenance

Need a very professional looking double sided Buisiness card with all my details phone number, name, email, license number.

Target Market(s)

construction industry

Industry/Entity Type

building

Contact Information for Business Card

Name Dale Whitcombe. Email Address Info@KPTBuilding.example.au mobile number 0452918730 licence number 871406D. web site

```html
<!DOCTYPE html>
<html lang="en">
<head>
<meta charset="utf-8">
<title>KPT Building And Maintenance – Business Card</title>
<link rel="stylesheet" href="https://fonts.googleapis.com/css2?family=Michroma&family=Roboto:wght@400&display=swap">
<style>
  :root {
    --backdrop: #b3b3b3;
    --card: #ffffff;
    --ink: #4a4a4b;
    --blue: #06a3e6;
  }
  * { margin: 0; padding: 0; box-sizing: border-box; }
  html, body { width: 1000px; height: 1200px; overflow: hidden; }
  body { background: var(--backdrop); position: relative; font-family: "Roboto", Arial, sans-serif; color: var(--ink); }
  .card { position: absolute; left: 50px; width: 899px; height: 540px; background: var(--card); }
  .card--front { top: 43px; }
  .card--back { top: 617px; }

  .brand { position: absolute; display: flex; align-items: center; gap: 16px; }
  .brand__mark { flex: none; background: var(--blue); }
  .brand__name { font-family: "Michroma", Arial, sans-serif; color: var(--ink); line-height: 1.15; text-transform: uppercase; }

  .card--front .brand { left: 81px; top: 92px; }
  .card--front .brand__mark { width: 70px; height: 70px; }
  .card--front .brand__name { font-size: 25px; }

  .card--back .brand { left: 100px; top: 230px; }
  .card--back .brand__mark { width: 86px; height: 86px; }
  .card--back .brand__name { font-size: 34px; }

  .contact { position: absolute; left: 523px; top: 290px; }
  .contact__name { font-family: "Michroma", Arial, sans-serif; font-size: 26px; letter-spacing: 1px; text-transform: uppercase; margin-bottom: 14px; }
  .contact__row { display: flex; align-items: center; gap: 11px; height: 29px; margin-bottom: 17px; font-size: 21.5px; }
  .contact__icon { width: 29px; height: 29px; border-radius: 4px; background: var(--blue); display: flex; align-items: center; justify-content: center; flex: none; }
  .contact__licence { font-size: 21.5px; margin-top: -7px; }
</style>
</head>
<body>
  <section class="card card--front">
    <div class="brand">
      <span class="brand__mark"></span>
      <span class="brand__name">KPT Building<br>And Maintenance</span>
    </div>

    <div class="contact">
      <h1 class="contact__name">Dale Whitcombe</h1>
      <div class="contact__row">
        <span class="contact__icon">
          <svg width="18" height="20" viewBox="0 0 18 20" fill="none" stroke="#fff" stroke-width="1.5"><rect x="4" y="1.5" width="10" height="17" rx="1.5" transform="rotate(20 9 10)"/></svg>
        </span>
        <span>0452918730</span>
      </div>
      <div class="contact__row">
        <span class="contact__icon">
          <svg width="20" height="14" viewBox="0 0 20 14" fill="none" stroke="#fff" stroke-width="1.5"><rect x="1" y="1" width="18" height="12"/><path d="M1 1l9 7 9-7M1 13l6.5-6M19 13l-6.5-6"/></svg>
        </span>
        <span>Info@KPTBuilding.example.au</span>
      </div>
      <div class="contact__row">
        <span class="contact__icon">
          <svg width="18" height="18" viewBox="0 0 18 18" fill="none" stroke="#fff" stroke-width="1.3"><circle cx="9" cy="9" r="7.5"/><ellipse cx="9" cy="9" rx="3.3" ry="7.5"/><path d="M1.5 9h15M3 5h12M3 13h12"/></svg>
        </span>
        <span>KPTBuilding.example.au</span>
      </div>
      <p class="contact__licence">Licence Number 871406D</p>
    </div>
  </section>

  <section class="card card--back">
    <div class="brand">
      <span class="brand__mark"></span>
      <span class="brand__name">KPT Building<br>And Maintenance</span>
    </div>
  </section>
</body>
</html>
```